Sports Event Company designing web home page

Design a home page for a Sports event company. Our company is launching an innovative new sports event (quite similiar to adult tag rugby) and we need a slick , kool , innovative website to help us launch our event . Our website needs to portray us as an energetic sports company but yet give a level of professionalism and reassurance despite our product been new.

We have built a Registration system but have encountered that the better website developers are not necessarilt the best designers.

Target Market(s)

20 to 35 year olds who are sporty . Sports and social commitees from corporates

Industry/Entity Type

Adult

Requirements
Must have
• Strong ability to interact with social media

Easy to register for events

Bright but classy

Colour scheme transferrable to Flyers , posters etc

```html
<!DOCTYPE html>
<html lang="en">
<head>
<meta charset="utf-8">
<title>Tag Velocity — Home</title>
<link href="https://fonts.googleapis.com/css2?family=Arimo:wght@400;700&family=PT+Sans:wght@700&display=swap" rel="stylesheet">
<style>
:root{
  --topbar:#230804;
  --red:#c8161d;
  --red-dark:#8c0d0c;
  --red-deep:#5a0806;
  --orange:#f2a13a;
  --yellow:#f6d35a;
  --cream:#fde9a6;
  --ink:#222;
  --muted:#777;
  --link-red:#c0141b;
  --panel-line:#d6d6d6;
  --white:#fff;
}
*{box-sizing:border-box;margin:0;padding:0}
html,body{width:709px;height:1200px;overflow:hidden}
body{position:relative;font-family:"Arimo",Arial,sans-serif;font-size:9px;color:var(--ink);background:#fff}
.abs{position:absolute}
a{color:inherit;text-decoration:none}

.topbar{left:0;top:0;width:709px;height:20px;background:var(--topbar);color:#eee;font-size:9px}
.topbar .links{left:36px;top:5px;display:flex;gap:8px}
.topbar .links span.dot{color:#aaa}
.topbar .phone{left:462px;top:3px;display:flex;align-items:center;gap:6px;font-weight:700;color:#fff}
.topbar .help{left:557px;top:3px;display:flex;align-items:center;gap:6px;font-weight:700;color:#fff}
.topbar .flags{left:640px;top:6px;display:flex;gap:8px}
.flag{width:13px;height:8px}

.header{left:0;top:20px;width:709px;height:65px;background:linear-gradient(90deg,#d22a1e 0%,#e7652b 30%,var(--yellow) 52%,#e9722c 72%,#cc1f1a 100%)}
.brand{left:48px;top:24px;display:flex;align-items:center;gap:6px}
.brand .mark{width:16px;height:16px;border-radius:50%;background:var(--red-deep)}
.brand .name{font-weight:700;font-size:10px;color:var(--red-deep)}
.sitetitle{left:175px;top:16px;font-family:"PT Sans",Arial,sans-serif;font-size:28px;color:#fff;letter-spacing:1px}
.search{display:flex;height:20px;width:195px;border-radius:10px;overflow:hidden;background:#fff;border:1px solid #b33}
.search .field{flex:1;padding:5px 12px;color:#555;font-size:9px}
.search .go{width:28px;background:linear-gradient(#b2161a,#6a0907);color:#fff;font-size:9px;display:flex;align-items:center;justify-content:center}

.nav{left:0;top:85px;width:709px;height:30px;background:linear-gradient(#b51c16,#7a0b08);border-bottom:2px solid #4a0604}
.nav ul{list-style:none;display:flex;position:absolute;left:58px;top:0;height:30px;align-items:center}
.nav li{color:#fff;font-weight:700;font-size:10px;margin-right:31px}
.nav li.active{background:linear-gradient(#ff3a2e,#c4140f);padding:4px 11px;border-radius:3px 3px 0 0;margin-right:24px;margin-left:-10px}

.backdrop{left:0;top:117px;width:709px;height:120px;background:linear-gradient(#9a9a9a,#e8e8e8 70%,#fff)}
.page{left:35px;top:131px;width:640px;height:865px;background:#fff;border-radius:14px 14px 0 0}

.hero{left:42px;top:138px;width:626px;height:202px}
.hero .photo{position:absolute;top:0;height:167px}
.hero .p1{left:0;width:225px;background:linear-gradient(#4fa5ea,#b9dcf4 65%,#9fd27a)}
.hero .p2{left:225px;width:173px;background:linear-gradient(#f4f4f4,#e4dad2)}
.hero .p3{left:398px;width:228px;background:linear-gradient(#4fa5ea,#b9dcf4 65%,#9fd27a)}
.hero .caption{position:absolute;left:0;top:167px;width:626px;height:35px;background:#2b2b2b}
.hero .caption h2{position:absolute;left:8px;top:9px;color:#f6c524;font-size:17px;font-weight:700}
.hero .caption p{position:absolute;left:226px;top:5px;width:395px;color:#fff;font-size:8.5px;line-height:12px}

.pager-top{left:571px;top:355px;font-size:8.5px;color:var(--muted)}
.pager-top b{color:var(--link-red);font-weight:400}

.cats{left:41px;top:360px;width:139px;height:258px;background:var(--cream);border-radius:6px;border:1px solid #e8c873}
.cats h3{height:18px;background:linear-gradient(#e43a2c,#b3130f);color:#fff;font-size:10px;text-align:center;padding-top:3px;border-radius:6px 6px 0 0}
.cats ul{list-style:none;margin:10px 5px 0}
.cats li{height:20px;padding:3px 22px;font-weight:700;font-size:8px;border-bottom:1px solid #e7cf8e}
.cats li.current{color:var(--link-red)}

.news-box{left:41px;top:628px;width:139px;height:218px;background:#f4f4f4;border:1px solid #ddd;border-radius:6px}
.news-box p{position:absolute;left:0;top:8px;width:137px;text-align:center;font-size:9.5px;line-height:12px;color:#444}
.news-box .input{position:absolute;left:9px;top:40px;width:119px;height:18px;background:#fff;border:1px solid #bbb}
.news-box .join{position:absolute;left:40px;top:63px;width:59px;height:16px;background:linear-gradient(#e2231a,#a40e0a);color:#fff;font-weight:700;font-size:9px;text-align:center;padding-top:3px;border-radius:2px}
.social{position:absolute;left:10px;width:120px;display:flex;align-items:center;gap:19px;font-size:8.5px;line-height:10px;color:#333}
.social i{width:21px;height:21px;border-radius:50%;flex:none}
.social .tw{background:#2d8fd6}.social .fb{background:#2f5d9e}.social .li{background:#1d6fa5}.social .em{background:#ea6a1f}

.latest-news{left:196px;top:375px}
.latest-news h2{font-size:12px;font-weight:700;color:#222}
.latest-news ul{list-style:none;position:absolute;left:1px;top:32px;width:260px}
.latest-news li{height:20px;font-size:8.5px;color:#777;white-space:nowrap}

.photos{left:466px;top:392px;width:168px;height:135px;border:1px solid #ccc;border-radius:4px;background:#fff;box-shadow:0 1px 2px #ccc}
.photos h3{font-size:10px;font-weight:700;margin:6px 0 0 6px}
.photos .grid{position:absolute;left:2px;top:22px;display:grid;grid-template-columns:repeat(3,53px);gap:2px}
.photos .grid div{height:53px}

.fixtures{left:258px;top:563px;width:337px;height:197px;border:1px solid #ccc;border-radius:4px;background:#fff;box-shadow:0 1px 3px #bbb}
.fixtures h3{font-size:10px;font-weight:400;margin:8px 0 0 3px;color:#222}
.fixtures h4{font-size:9px;font-weight:700;margin:4px 0 6px 8px}
.fixtures table{border-collapse:collapse;margin-left:3px;width:330px;font-size:8px}
.fixtures td{height:12px;padding:0 0 0 1px;white-space:nowrap}
.fixtures tr:nth-child(even) td{background:#ececec}
.fixtures .regions{position:absolute;left:40px;top:172px;width:255px;border-top:1px solid #bbb;padding-top:6px;text-align:center;font-size:8px;color:#333}

.pager{left:373px;top:802px;display:flex;gap:6px;align-items:center;font-size:8.5px;color:var(--link-red)}
.pager .on{background:var(--link-red);color:#fff;width:13px;height:13px;text-align:center;padding-top:1px}
.divider{left:197px;top:818px;width:470px;height:1px;background:#ddd}

.videos-title{left:203px;top:831px;font-size:12px;font-weight:700}
.videos{left:203px;top:854px;width:460px;height:121px;border:1px solid #ccc;border-radius:4px;background:linear-gradient(#fff,#f0f0f0)}
.arrow{width:22px;height:24px;background:linear-gradient(#888,#555);border-radius:2px}
.vid{position:absolute;top:15px;width:118px;text-align:center}
.vid .thumb{height:69px;position:relative}
.vid .play{position:absolute;left:47px;top:22px;width:26px;height:26px;border-radius:50%;background:rgba(40,40,40,.85)}
.vid p{color:var(--link-red);font-size:8px;line-height:10px;margin-top:7px}

.strip{left:0;top:998px;width:709px;height:40px;background:linear-gradient(#1c0705,#3b0c07)}
.strip .badge{left:44px;top:4px;width:32px;height:32px;border-radius:50%;background:linear-gradient(#d9d7a0,#8d9b3f)}
.strip .secure{left:82px;top:15px;color:#fff;font-weight:700;font-size:9px}
.strip .box{left:274px;top:8px;width:26px;height:24px;background:#c87a3a;border-radius:2px}
.strip .sched{left:307px;top:15px;color:#fff;font-weight:700;font-size:9px}

.footer{left:0;top:1038px;width:709px;height:162px;background:linear-gradient(#a21812,#7a0d09 60%,#6c0b07)}
.col{position:absolute;top:22px;color:#fff;font-size:8.5px}
.col h4{font-size:10px;font-weight:700;margin-bottom:13px}
.col li{list-style:none;height:13.3px}
.col .hl{color:#ffd24a}
</style>
</head>
<body>

<div class="abs topbar">
  <div class="abs links"><a>Account Sign In</a><span class="dot">•</span><a>Register</a><span class="dot">•</span><a>About</a><span class="dot">•</span><a>Blog</a><span class="dot">•</span><a>Contact</a></div>
  <div class="abs phone"><svg width="11" height="13" viewBox="0 0 11 13"><path d="M2 1l2 0 1 3-1.5 1c.6 1.6 1.6 2.8 3 3.5L8 7l3 1v2.5c0 1-1 1.5-2 1.3C4.5 11 1 7 .5 3 .4 1.8 1 1 2 1z" fill="#f07a1e"/></svg>123.456.7890</div>
  <div class="abs help"><svg width="20" height="13" viewBox="0 0 20 13"><ellipse cx="10" cy="6" rx="10" ry="5.5" fill="#6fc23a"/><path d="M5 10l-1 3 4-2z" fill="#6fc23a"/></svg>Help</div>
  <div class="abs flags">
    <svg class="flag" viewBox="0 0 13 8"><rect width="13" height="8" fill="#fff"/><rect width="3.3" height="8" fill="#d52b1e"/><rect x="9.7" width="3.3" height="8" fill="#d52b1e"/><circle cx="6.5" cy="4" r="1.5" fill="#d52b1e"/></svg>
    <svg class="flag" viewBox="0 0 13 8"><rect width="13" height="8" fill="#fff"/><g fill="#b22234"><rect width="13" height="1"/><rect y="2" width="13" height="1"/><rect y="4" width="13" height="1"/><rect y="6" width="13" height="1"/></g><rect width="6" height="4" fill="#3c3b6e"/></svg>
  </div>
</div>

<header class="abs header">
  <div class="abs brand"><span class="mark"></span><span class="name">KORA TAG LEAGUE</span></div>
  <div class="abs sitetitle">TAG VELOCITY</div>
  <div class="abs search" style="left:480px;top:23px"><span class="field">Search website</span><span class="go">GO</span></div>
</header>

<nav class="abs nav">
  <ul>
    <li class="active">HOME</li><li>PLAY TAG RUGBY</li><li>NEWS</li><li>PLAYERS</li><li>SOCIAL</li><li>COACHING</li><li>PARTNERS &amp; SPONSORS</li><li>LINKS</li>
  </ul>
</nav>

<div class="abs backdrop"></div>
<div class="abs page"></div>

<section class="abs hero">
  <div class="photo p1" role="img" aria-label="Player crouching to pick up a ball on a grass field under a blue sky"></div>
  <div class="photo p2" role="img" aria-label="Player in a white kit running with the ball"></div>
  <div class="photo p3" role="img" aria-label="Player in sunglasses tossing a ball, blue sky behind"></div>
  <div class="caption">
    <h2>RELIVE ALL THE ACTION</h2>
    <p>worldtagcup Results of last week's video poll and here are highlights from Russia's final pool match of. #wtc2011 tg.ly/HPkFA9 #wtc2015</p>
  </div>
</section>

<div class="abs pager-top">Page: &nbsp;1 / 2 / <b>3</b> / <b>4</b> / <b>5</b></div>

<aside class="abs cats">
  <h3>Browse Categories</h3>
  <ul>
    <li>History</li><li class="current">Teams</li><li>Statistics</li><li>News</li><li>Photos</li><li>Video</li><li>Media Center</li><li>Tickets</li><li>Fan Zone</li><li>Organisation</li><li>Worldwide Partners</li>
  </ul>
</aside>

<aside class="abs news-box">
  <p>Join our newsletter list<br>to get the latest updates</p>
  <div class="input"></div>
  <div class="join">Join Now</div>
  <div class="social" style="top:93px"><i class="tw"></i><span>Follow us on Chirper</span></div>
  <div class="social" style="top:123px"><i class="fb"></i><span>Become our fan<br>on FaceSpace</span></div>
  <div class="social" style="top:156px"><i class="li"></i><span>Connect with us<br>on LinkPro</span></div>
  <div class="social" style="top:188px"><i class="em"></i><span>Send us your<br>email enquiries</span></div>
</aside>

<section class="abs latest-news">
  <h2>LATEST NEWS...</h2>
  <ul>
    <li>&gt;&gt; &nbsp;Ewan Harlow sets Japan on path to WTC 2019</li>
    <li>&gt;&gt; &nbsp;Marchetti: A momentous night in Mexico</li>
    <li>&gt;&gt; &nbsp;Mexico on the climb in world rankings</li>
    <li>&gt;&gt; &nbsp;Mexico off to flyer in WTC 2015 qualifying</li>
    <li>&gt;&gt; &nbsp;Qualifying process set for thrilling start</li>
    <li>&gt;&gt; &nbsp;The golden age of Caribbean rugby</li>
  </ul>
</section>

<section class="abs photos">
  <h3>Latest Photos</h3>
  <div class="grid">
    <div role="img" aria-label="Players in a tackle" style="background:linear-gradient(#3a4a7a,#7a5a4a)"></div>
    <div role="img" aria-label="Player diving on grass" style="background:linear-gradient(#c8c8c8,#5e9a4a)"></div>
    <div role="img" aria-label="Players in red and white kits" style="background:linear-gradient(#d8d0c8,#a03030)"></div>
    <div role="img" aria-label="Players in green kits" style="background:linear-gradient(#6a8a5a,#2a6a3a)"></div>
    <div role="img" aria-label="Team group on the pitch" style="background:linear-gradient(#a8b8c8,#7a6a6a)"></div>
    <div role="img" aria-label="Squad posing in blue" style="background:linear-gradient(#5a7ab8,#3a5a9a)"></div>
  </div>
</section>

<section class="abs fixtures">
  <h3>Fixtures &amp; Results</h3>
  <h4>Latest Results</h4>
  <table>
    <tr><td>18 Apr 2012</td><td>Philippines</td><td>34 - 12</td><td>Chinese Taipei</td><td>Harbour Park Stadium</td></tr>
    <tr><td>18 Apr 2012</td><td>Sri Lanka</td><td>35 - 10</td><td>Singapore</td><td>Harbour Park Stadium</td></tr>
    <tr><td>15 Apr 2012</td><td>Singapore</td><td>20 - 37</td><td>Philippines</td><td>Harbour Park Stadium</td></tr>
    <tr><td>15 Apr 2012</td><td>Sri Lanka</td><td>36 - 8</td><td>Chinese Taipei</td><td>Harbour Park Stadium</td></tr>
  </table>
  <h4 style="margin-top:8px">Upcoming Fixtures</h4>
  <table>
    <tr><td>21 Apr 2012</td><td>Barbados</td><td>-</td><td>SVG</td><td>Palm Bay Oval</td></tr>
    <tr><td>21 Apr 2012</td><td>Cayman Islands</td><td>-</td><td>Mexico</td><td>George Town</td></tr>
    <tr><td>21 Apr 2012</td><td>Sri Lanka</td><td>-</td><td>Philippines</td><td>Harbour Park Stadium</td></tr>
    <tr><td>21 Apr 2012</td><td>Singapore</td><td>-</td><td>Chinese Taipei</td><td>Harbour Park Stadium</td></tr>
  </table>
  <div class="regions">AFRICA | AMERICAS | ASIA | EUROPE | OCEANIA | REPECHAGE</div>
</section>

<div class="abs pager"><span class="on">1</span><span>2</span><span>3</span><span>4</span><span>5</span><span>Next &gt;</span><span>&nbsp;Last &gt;&gt;</span></div>
<div class="abs divider"></div>

<h2 class="abs videos-title">LATEST VIDEOS</h2>
<section class="abs videos">
  <div class="vid" style="left:29px"><div class="thumb" role="img" aria-label="Video still of players contesting the ball" style="background:linear-gradient(#5a6a3a,#c8b040 60%,#3a5a2a)"><span class="play"></span></div><p>WTC 2015 qualifying<br>promo</p></div>
  <div class="vid" style="left:168px"><div class="thumb" role="img" aria-label="Video player showing a tackle on a green pitch" style="background:linear-gradient(#1a2a5a,#2a6a3a 50%,#1a2a5a)"><span class="play"></span></div><p>Listen to the Weekly<br>Programme</p></div>
  <div class="vid" style="left:308px"><div class="thumb" role="img" aria-label="Video still of players contesting the ball" style="background:linear-gradient(#5a6a3a,#c8b040 60%,#3a5a2a)"><span class="play"></span></div><p>WTC 2015 qualifying<br>promo</p></div>
</section>
<svg class="abs arrow" style="left:199px;top:896px" viewBox="0 0 22 24"><rect width="22" height="24" rx="2" fill="#666"/><path d="M13 7l-5 5 5 5z" fill="#fff"/></svg>
<svg class="abs arrow" style="left:643px;top:896px" viewBox="0 0 22 24"><rect width="22" height="24" rx="2" fill="#666"/><path d="M9 7l5 5-5 5z" fill="#fff"/></svg>

<div class="abs strip">
  <div class="abs badge"></div>
  <div class="abs secure">This Website is safely &amp; securely</div>
  <div class="abs box"></div>
  <div class="abs sched">World Tag Cup Schedule</div>
  <div class="abs search" style="left:480px;top:10px"><span class="field">Search website</span><span class="go">GO</span></div>
</div>

<footer class="abs footer">
  <div class="col" style="left:49px"><h4>Website</h4><ul><li>Home</li><li>About Us</li><li>Blog</li><li>Latest News</li><li>Login</li><li>Join Us</li></ul></div>
  <div class="col" style="left:150px"><h4>Categories</h4><ul><li>Lorem ipsum dolor sit</li><li>Amet consectetur</li><li>Adipiscin elit</li><li>Cras suscipit lacus</li><li>Dapibus ante mattis</li><li>Adipiscing nibh placerat</li></ul></div>
  <div class="col" style="left:294px"><h4>Information</h4><ul><li>My Account</li><li>Disclaimer</li><li>Terms &amp; Conditions</li><li>Privacy Policy</li><li>FAQ</li></ul></div>
  <div class="col" style="left:423px"><h4>Social Network</h4><ul><li>My Account</li><li>Rewards</li><li>Terms &amp; Conditions</li><li>Help</li><li>FAQ</li></ul></div>
  <div class="col" style="left:553px"><h4>Contact Us</h4><ul><li>Phone: 1.234.567.8901</li><li>Toll-Free: 1.234.567.8901</li><li></li><li>Fax: 1.234.567.8901</li><li>Email: <span class="hl">Send us an email</span></li></ul></div>
</footer>

</body>
</html>
```